Real Estate Business Cards

Looking for a clean, sharp and professional look for our Real Estate investment Fund that invests in Multi Family Apartment buildings.

Target Market(s)

Real Estate Fund

Industry/Entity Type

Real Estate

Contact Information for Business Card

Company Description: Real Estate Investment Fund
Company Name: RKW Holdings
Name: Marcus Olvane
Cell: (917) 482-0657
Email: marcus@rkwholdings-example.com
Website: www.rkwholdings-example.com
Address: 418, 9th Street, Brooklyn NY 11218

Colors

Designer to choose colors to be used in the design.

Requirements
Nice to have
• Colors to match logo

```html
<!DOCTYPE html>
<html lang="en">
<head>
<meta charset="utf-8">
<title>RKW Holdings – Business Card</title>
<link href="https://fonts.googleapis.com/css2?family=Lato:wght@400;700&family=Cinzel:wght@400&display=swap" rel="stylesheet">
<style>
  :root {
    --brand-blue: #1b75b9;
    --brand-blue-dark: #1666a3;
    --ink: #3a3a3a;
    --paper: #ffffff;
    --backdrop: #e9ebee;
  }
  * { margin: 0; padding: 0; box-sizing: border-box; }
  html, body { width: 1200px; height: 835px; overflow: hidden; }
  body {
    background: var(--backdrop);
    font-family: "Lato", sans-serif;
    position: relative;
  }
  .card {
    position: absolute;
    width: 540px;
    height: 309px;
    border-radius: 18px;
    overflow: hidden;
    box-shadow: 0 6px 18px rgba(0,0,0,0.18);
  }
  /* Front */
  .card-front { left: 40px; top: 263px; background: var(--paper); }
  .side-band {
    position: absolute; left: 0; top: 0; bottom: 0; width: 66px;
    background: var(--brand-blue);
  }
  .brand {
    position: absolute; left: 84px; top: 42px;
    display: flex; align-items: center; gap: 12px;
  }
  .brand-mark {
    width: 30px; height: 30px; background: var(--brand-blue);
  }
  .brand-name {
    font-family: "Cinzel", serif;
    font-size: 26px; color: var(--brand-blue); letter-spacing: 1px;
  }
  .name-tag {
    position: absolute; right: 0; top: 62px;
    background: var(--brand-blue); color: var(--paper);
    font-weight: 700; font-size: 18px;
    padding: 7px 24px 7px 22px;
    border-radius: 20px 0 0 20px;
  }
  .contact-list {
    position: absolute; left: 48px; top: 178px;
    list-style: none; font-size: 14px; color: var(--ink); line-height: 23px;
  }
  .contact-list li { display: flex; align-items: center; gap: 8px; }
  .contact-icon {
    width: 18px; height: 18px; background: var(--paper);
    border-radius: 3px; display: flex; align-items: center; justify-content: center;
  }
  .company-block {
    position: absolute; left: 240px; top: 228px; text-align: center; color: var(--ink);
  }
  .company-name { font-weight: 700; color: var(--brand-blue); font-size: 15px; }
  .company-address { font-size: 14px; margin-top: 2px; }
  /* Back */
  .card-back { left: 620px; top: 263px; background: var(--brand-blue); }
  .back-pattern {
    position: absolute; inset: 0;
    background: linear-gradient(135deg, var(--brand-blue) 0%, var(--brand-blue-dark) 100%);
  }
  .tagline {
    position: absolute; left: 0; right: 0; top: 50%;
    transform: translateY(-50%);
    text-align: center; color: var(--paper);
    font-weight: 700; font-size: 24px; letter-spacing: 0.5px;
  }
</style>
</head>
<body>
  <section class="card card-front">
    <div class="side-band"></div>
    <div class="brand">
      <span class="brand-mark"></span>
      <span class="brand-name">RKW Holdings</span>
    </div>
    <div class="name-tag">Marcus Olvane</div>
    <ul class="contact-list">
      <li>
        <span class="contact-icon">
          <svg width="10" height="14" viewBox="0 0 10 14"><rect x="1" y="1" width="8" height="12" rx="1.5" fill="none" stroke="#1b75b9" stroke-width="1.5"/><circle cx="5" cy="11" r="0.9" fill="#1b75b9"/></svg>
        </span>
        (917) 482-0657
      </li>
      <li>
        <span class="contact-icon">
          <svg width="14" height="10" viewBox="0 0 14 10"><rect x="0.75" y="0.75" width="12.5" height="8.5" fill="none" stroke="#1b75b9" stroke-width="1.5"/><path d="M1 1l6 5 6-5" fill="none" stroke="#1b75b9" stroke-width="1.5"/></svg>
        </span>
        marcus@rkwholdings-example.com
      </li>
      <li>
        <span class="contact-icon">
          <svg width="14" height="14" viewBox="0 0 14 14"><circle cx="7" cy="7" r="6" fill="none" stroke="#1b75b9" stroke-width="1.4"/><path d="M1 7h12M7 1c-3 3-3 9 0 12M7 1c3 3 3 9 0 12" fill="none" stroke="#1b75b9" stroke-width="1.1"/></svg>
        </span>
        www.rkwholdings-example.com
      </li>
    </ul>
    <div class="company-block">
      <div class="company-name">RKW Holdings</div>
      <div class="company-address">418, 9th Street, Brooklyn NY 11218</div>
    </div>
  </section>

  <section class="card card-back">
    <div class="back-pattern" role="img" aria-label="Repeating brand pattern in light blue tones"></div>
    <p class="tagline">Real Estate Investment Fund</p>
  </section>
</body>
</html>
```